Hearthbloom Living is an online store specialising in all things for the home Bathroom, Kitchen,

I need a business card designed that is professional and elegant, yet not conservative. We will be wanting to brand the entire business and will have videos made where we will be interacting with the product, testing the products and basically creating an online interactive community for all those people interested in all things to do with the Home and the activities that take place in and around the home.

Target Market(s)

30-65yr old Men and Women who LOVE their Home and see it as their primary place of Happiness, their sanctuary!

Industry/Entity Type

Business

Contact Information for Business Card

www.hearthbloomliving.example Hearthbloom Living-PO Box 58391, Mt Ferndale, Auckland. NEW ZEALAND. info@hearthbloomliving.example
Love your Home! Lorraine Becker-Duponte

Font styles to use
Decorative
Script

Colors
9bcb3b
33b8a4
85cae6
b7a5cd
eda3c7
e667a6
d2a4cc
fdf9cf
fee18a

Requirements
Must have
• Attractive colours. Must feel Elegant, yet simple. A font that is rounded without sharp edges. Organic feel to the card, something raw with texture.
Nice to have
• I like the logo deign that I gave in the photos, something feminine, but fun.
Should not have
• I dont like sharp edges, or linear design. I like organic, flowing, fractal type design. Something that looks beautiful in form when you look at it.

```html
<!DOCTYPE html>
<html lang="en">
<head>
<meta charset="utf-8">
<title>Hearthbloom Living – Business Card</title>
<link rel="stylesheet" href="https://fonts.googleapis.com/css2?family=Lobster&family=Montserrat:wght@400;500;600&display=swap">
<style>
  :root {
    --page-bg: #ecebe8;
    --stripe-blue: #85cae6;
    --stripe-black: #111111;
    --rose-pink: #e0257f;
    --rose-deep: #b8155f;
    --leaf-green: #7cc13a;
    --gold: #c9a545;
    --brand-blue: #4fa3cf;
    --brand-pink: #e64aa0;
    --ink: #2a2a2a;
    --card-white: #ffffff;
  }
  * { box-sizing: border-box; margin: 0; padding: 0; }
  html, body {
    width: 1200px; height: 1200px; overflow: hidden;
    background: var(--page-bg);
  }
  .sheet {
    width: 1200px; height: 1200px;
    display: flex; flex-direction: column; align-items: center; justify-content: center;
    gap: 60px;
  }
  .card {
    position: relative;
    width: 840px; height: 480px;
    border-radius: 6px;
    overflow: hidden;
    box-shadow: 0 10px 28px rgba(0,0,0,0.18);
  }

  /* Front */
  .card-front {
    background: repeating-linear-gradient(
      to bottom,
      var(--stripe-blue) 0 48px,
      var(--stripe-black) 48px 96px
    );
  }
  .roses {
    position: absolute;
    border-radius: 48% 52% 45% 55% / 55% 45% 55% 45%;
    background: radial-gradient(circle at 40% 40%, var(--rose-pink), var(--rose-deep) 70%, var(--leaf-green) 100%);
  }
  .roses-top { top: -60px; right: -40px; width: 320px; height: 180px; }
  .roses-bottom { bottom: -60px; left: -50px; width: 400px; height: 200px; }
  .name-plate {
    position: absolute;
    left: 50%; top: 50%;
    transform: translate(-50%, -50%);
    width: 420px; height: 220px;
    background: var(--card-white);
    border: 5px solid var(--gold);
    display: flex; align-items: center; justify-content: center;
    text-align: center;
  }
  .brand-name {
    font-family: "Montserrat", sans-serif;
    font-weight: 500;
    font-size: 36px;
    line-height: 1.25;
    letter-spacing: 0.04em;
    color: var(--brand-blue);
  }

  /* Back */
  .card-back {
    background: var(--card-white);
    display: flex; flex-direction: column; align-items: center;
    padding-top: 56px;
    text-align: center;
  }
  .tagline {
    font-family: "Montserrat", sans-serif;
    font-weight: 500;
    font-size: 16px;
    letter-spacing: 0.12em;
    color: var(--ink);
  }
  .person-name {
    font-family: "Lobster", cursive;
    font-weight: 400;
    font-size: 52px;
    line-height: 1.2;
    margin-top: 6px;
    color: var(--brand-blue);
  }
  .person-name .surname { color: var(--brand-pink); }
  .contact {
    list-style: none;
    margin-top: 10px;
    font-family: "Montserrat", sans-serif;
    font-weight: 400;
    font-size: 16px;
    line-height: 1.6;
    letter-spacing: 0.08em;
    text-transform: uppercase;
    color: var(--ink);
  }
  .rose-sprig {
    width: 80px; height: 44px; margin-top: 14px;
    border-radius: 50%;
    background: radial-gradient(circle at 35% 50%, var(--rose-pink), var(--rose-deep) 55%, var(--leaf-green) 100%);
  }
  .brand-line {
    margin-top: 16px;
    font-family: "Montserrat", sans-serif;
    font-weight: 500;
    font-size: 28px;
    letter-spacing: 0.06em;
    color: var(--brand-blue);
  }
</style>
</head>
<body>
<main class="sheet">
  <section class="card card-front" aria-label="Card front">
    <div class="roses roses-top" role="img" aria-label="Cluster of pink roses with green leaves"></div>
    <div class="roses roses-bottom" role="img" aria-label="Bouquet of deep pink roses with green leaves"></div>
    <div class="name-plate">
      <p class="brand-name">Hearthbloom<br>Living</p>
    </div>
  </section>

  <section class="card card-back" aria-label="Card back">
    <p class="tagline">LOVE YOUR HOME</p>
    <h1 class="person-name">Lorraine Becker<span class="surname">-Duponte</span></h1>
    <ul class="contact">
      <li>PO Box 58391</li>
      <li>Mt Ferndale, Auckland, New Zealand</li>
      <li>info@hearthbloomliving.example</li>
      <li>www.hearthbloomliving.example</li>
    </ul>
    <div class="rose-sprig" role="img" aria-label="Small sprig of two pink roses"></div>
    <p class="brand-line">Hearthbloom Living</p>
  </section>
</main>
</body>
</html>
```